Redesign responsive website and logo for webshop platform

Redesign our applications old website with a new clean, crisp modern looking style that is responsive.

Our application is a cloud based, free ecommerce platform that lets users set up their own webshops within minutes. (Similar to Bramvik https://bramvik.example/l/sell)

Our old website: http://sv.kelporia.example/

I need redesigned HTML + CSS for the following three pages:
* Landing Page:
(Old page: http://sv.kelporia.example/)
I have attached a mockup of a proposed layout/structure for the landing page.
- Pricing comparision/features page
(Old page http://sv.kelporia.example/t/funktioner)
- Generic "article" page:
(Old page http://sv.kelporia.example/d/redigerasida)

The pages must responsive using HTML 5/CSS 3 (I prefer Bootstrap 3 if possible).

I also need a redesign of the logotype.

If you have any questions don't hesitate to ask and we will provide whatever is needed to you.

Logo Text

Kelporia

Coding

Coded - Design and coding required

Number of Pages Required

3 page

Font styles to use
Serif
Sans Serif

```html
<!DOCTYPE html>
<html lang="en">
<head>
<meta charset="utf-8">
<title>Kelporia – Start a free webshop</title>
<link href="https://fonts.googleapis.com/css2?family=Roboto+Condensed:wght@400;700&family=Open+Sans:wght@400;600;700&family=Roboto:wght@400;500&display=swap" rel="stylesheet">
<style>
:root{
  --blue:#1591d4;
  --blue-dark:#0f7fc0;
  --ink:#2b2b2b;
  --navy:#1e2a44;
  --muted:#6d6d6d;
  --tile-dark:#3b3b3b;
  --footer:#1e1e1e;
  --soft:#f3f3f1;
  --white:#ffffff;
}
*{margin:0;padding:0;box-sizing:border-box}
html,body{width:1200px;height:2436px;overflow:hidden}
body{font-family:"Open Sans",Arial,sans-serif;color:var(--ink);background:var(--white);position:relative}
.abs{position:absolute}

/* hero */
.hero{position:absolute;left:0;top:0;width:1200px;height:607px;
  background:linear-gradient(180deg,#5c6268 0%,#41464b 45%,#2a2d30 78%,#1f2123 100%);overflow:hidden}
.hero-photo{position:absolute;inset:0;background:
  radial-gradient(ellipse at 60% 30%,rgba(180,188,196,.35),transparent 60%),
  linear-gradient(180deg,rgba(0,0,0,0) 70%,rgba(0,0,0,.35) 100%)}
.brand{font-family:"Open Sans",sans-serif;font-weight:700;color:var(--white);font-size:34px;letter-spacing:.5px}
.hero .brand{left:97px;top:36px}
.btn-login{left:990px;top:36px;width:77px;height:31px;border:1px solid rgba(255,255,255,.85);color:var(--white);
  font-family:"Roboto",sans-serif;font-size:14px;display:flex;align-items:center;justify-content:center}
.menu-toggle{left:1083px;top:42px}
.hero-title{left:0;width:1200px;top:232px;text-align:center;color:var(--white);font-family:"Roboto Condensed",sans-serif;font-weight:700;font-size:40px}
.hero-text{left:330px;width:540px;top:288px;text-align:center;color:#f1f1f1;font-family:"Roboto",sans-serif;font-size:16px;line-height:22px}
.btn-cta{left:464px;top:370px;width:272px;height:41px;background:var(--blue);color:var(--white);
  font-family:"Roboto Condensed",sans-serif;font-size:17px;display:flex;align-items:center;justify-content:center}

/* welcome */
.section-title{font-family:"Roboto Condensed",sans-serif;font-weight:400;text-align:center;width:1200px;left:0}
.welcome-title{top:648px;font-size:37px;color:var(--ink)}
.welcome-title span{color:var(--blue)}
.welcome-text{left:150px;width:900px;top:705px;text-align:center;font-size:11.5px;line-height:21px;color:var(--muted)}

.tile{width:325px;height:206px;padding:26px 22px 0 23px;color:var(--white)}
.tile.blue{background:linear-gradient(135deg,#1c9ae0,#1287c9)}
.tile.dark{background:linear-gradient(135deg,#3f3f3f,#333)}
.tile-head{display:flex;align-items:flex-start;gap:12px;height:58px}
.tile-head svg{flex:none}
.tile-title{font-weight:700;font-size:19px;line-height:23px;text-transform:uppercase;padding-top:4px}
.tile-text{font-size:12.5px;line-height:18px;margin-top:8px;color:rgba(255,255,255,.92)}
.read-more{font-size:11.5px;font-weight:700;margin-top:12px;display:flex;align-items:center;gap:4px;text-transform:uppercase}

/* key features */
.features{position:absolute;left:0;top:1291px;width:1200px;height:496px;background:linear-gradient(90deg,#f6f6f4,#efefec)}
.feature-title{top:45px;font-size:31px;color:var(--navy)}
.feature-sub{top:93px;width:1200px;left:0;text-align:center;font-size:12.5px;color:var(--muted)}
.feature{width:330px;height:140px}
.feature-icon{position:absolute;left:0;top:0;width:84px;height:84px;border-radius:50%;border:1px solid #333;display:flex;align-items:center;justify-content:center;background:var(--white)}
.feature-name{position:absolute;left:98px;top:-6px;font-family:"Roboto",sans-serif;font-size:17.5px;color:#333}
.feature-text{position:absolute;left:98px;top:26px;width:220px;font-size:11.5px;line-height:20.5px;color:var(--muted)}
.feature-more{position:absolute;left:98px;top:98px;font-size:13.5px;color:#888}

/* news */
.news-title{left:97px;top:1840px;font-family:"Roboto Condensed",sans-serif;font-size:26px;color:var(--ink)}
.news-arrows{left:1055px;top:1848px}
.news-photo{width:187px;height:162px;top:1897px}
.news-body{top:1890px;width:260px}
.news-body h3{font-family:"Roboto",sans-serif;font-weight:400;font-size:17px;color:#333}
.news-date{margin-top:14px;font-size:12px;font-weight:700;font-style:italic;color:var(--blue)}
.news-body p{margin-top:8px;font-size:11.5px;line-height:20px;color:var(--muted)}
.news-more{margin-top:7px;font-size:13px;color:#333}

/* footer */
.footer{position:absolute;left:0;top:2111px;width:1200px;height:273px;background:var(--footer);color:var(--white)}
.footer .brand{left:97px;top:50px}
.contact{left:97px;top:104px;font-size:13px;line-height:19px}
.contact-row{display:flex;gap:14px;align-items:flex-start;margin-bottom:13px}
.footer h4{font-family:"Roboto",sans-serif;font-weight:400;font-size:16.5px;text-transform:uppercase}
.signup{left:408px;top:50px;width:290px}
.signup p{font-size:11px;line-height:19px;margin-top:16px}
.signup-input{margin-top:16px;width:286px;height:40px;background:var(--white);color:#444;font-size:11.5px;padding:12px 14px}
.btn-subscribe{margin-top:10px;width:100px;height:40px;background:var(--blue);font-size:13px;display:flex;align-items:center;justify-content:center;text-transform:uppercase}
.links{left:791px;top:50px}
.links ul{list-style:none;margin-top:22px;font-size:12.5px;line-height:24px}
.social{left:981px;top:50px}
.social ul{list-style:none;margin-top:18px;font-size:14px}
.social li{display:flex;align-items:center;gap:10px;height:36px}
.social .dot{width:26px;height:26px;border-radius:50%;border:1px solid rgba(255,255,255,.8)}
.copyright{position:absolute;left:0;top:2384px;width:1200px;height:52px;background:var(--blue);color:var(--white);
  font-size:12.5px;display:flex;align-items:center;justify-content:center}
</style>
</head>
<body>

<header class="hero">
  <div class="hero-photo" role="img" aria-label="Office desk with laptop, notebook and coffee mug in front of a window overlooking a city skyline"></div>
  <div class="abs brand">KELPORIA</div>
  <div class="abs btn-login">LOGIN</div>
  <svg class="abs menu-toggle" width="18" height="16" viewBox="0 0 18 16"><rect y="1" width="18" height="2.6" fill="#fff"/><rect y="6.7" width="18" height="2.6" fill="#fff"/><rect y="12.4" width="18" height="2.6" fill="#fff"/></svg>
  <h1 class="abs hero-title">START A FREE WEBSHOP</h1>
  <p class="abs hero-text">Kelporia is a service that allows you to launch a complete online store. The service is free and has everything needed to get you started with your business and sell products online.</p>
  <div class="abs btn-cta">CLICKS TO CREATE A WEBSHOP</div>
</header>

<h2 class="abs section-title welcome-title">WELCOME TO <span>KELPORIA</span></h2>
<p class="abs welcome-text">Sed ut perspiciatis unde omnis iste natus error sit voluptatem accusantium doloremque laudantium, totam rem aperiam, eaque ipsa quae ab illo inventore veritatis et quasi architecto beatae vitae dicta sunt explicabo. Nemo enim ipsam voluptatem quia voluptas sit aspernatur aut odit aut fugit, sed quia consequuntur magni dolores eos qui ratione voluptatem sequi nesciunt. Neque porro quisquam est, qui dolorem ipsum quia dolor sit amet, consectetur, adipisci velit.</p>

<div class="abs tile blue" style="left:97px;top:806px">
  <div class="tile-head"><svg width="44" height="44" viewBox="0 0 44 44"><circle cx="22" cy="22" r="18" fill="none" stroke="#fff" stroke-width="4"/><path d="M22 11v12h8" fill="none" stroke="#fff" stroke-width="4"/></svg><div class="tile-title">Get started<br>in 5 minutes</div></div>
  <p class="tile-text">Starting an E-cart with Kelporia takes no more than 5 minutes. Create an account to get started. Nothing needs to be installed on your computer.</p>
  <div class="read-more">Read more <svg width="11" height="11" viewBox="0 0 11 11"><circle cx="5.5" cy="5.5" r="5.5" fill="#fff"/><path d="M4.5 3l2.5 2.5L4.5 8" stroke="#1591d4" stroke-width="1.6" fill="none"/></svg></div>
</div>
<div class="abs tile dark" style="left:438px;top:806px">
  <div class="tile-head"><svg width="46" height="44" viewBox="0 0 46 44"><path d="M15 16l8-10 8 10" fill="none" stroke="#fff" stroke-width="3"/><rect x="2" y="16" width="42" height="6" fill="#fff"/><path d="M6 24h34l-4 16H10z" fill="#fff"/><path d="M16 27v10M23 27v10M30 27v10" stroke="#3b3b3b" stroke-width="2.5"/></svg><div class="tile-title">Create a free<br>online store</div></div>
  <p class="tile-text">Kelporia is a free service. The service has no monthly fees or transaction charges on what you sell.</p>
  <div class="read-more">Read more <svg width="11" height="11" viewBox="0 0 11 11"><circle cx="5.5" cy="5.5" r="5.5" fill="#fff"/><path d="M4.5 3l2.5 2.5L4.5 8" stroke="#3b3b3b" stroke-width="1.6" fill="none"/></svg></div>
</div>
<div class="abs tile blue" style="left:776px;top:806px">
  <div class="tile-head"><svg width="34" height="44" viewBox="0 0 34 44"><path d="M17 3a13 13 0 0 0-8 23v6h16v-6a13 13 0 0 0-8-23z" fill="none" stroke="#fff" stroke-width="3.5"/><rect x="10" y="35" width="14" height="3" fill="#fff"/><rect x="12" y="40" width="10" height="3" fill="#fff"/></svg><div class="tile-title">Intuitive user<br>interface</div></div>
  <p class="tile-text">It is fast to add new products. Organize products by drag and drop.</p>
  <div class="read-more">Read more <svg width="11" height="11" viewBox="0 0 11 11"><circle cx="5.5" cy="5.5" r="5.5" fill="#fff"/><path d="M4.5 3l2.5 2.5L4.5 8" stroke="#1591d4" stroke-width="1.6" fill="none"/></svg></div>
</div>

<div class="abs tile dark" style="left:97px;top:1030px">
  <div class="tile-head"><svg width="42" height="44" viewBox="0 0 42 44"><circle cx="17" cy="17" r="12" fill="none" stroke="#fff" stroke-width="5"/><path d="M26 26l12 12" stroke="#fff" stroke-width="6" stroke-linecap="round"/></svg><div class="tile-title">Search engine<br>optimized</div></div>
  <p class="tile-text">Kelporia is consistently created with search engine optimization as a focus point.</p>
  <div class="read-more">Read more <svg width="11" height="11" viewBox="0 0 11 11"><circle cx="5.5" cy="5.5" r="5.5" fill="#fff"/><path d="M4.5 3l2.5 2.5L4.5 8" stroke="#3b3b3b" stroke-width="1.6" fill="none"/></svg></div>
</div>
<div class="abs tile blue" style="left:438px;top:1030px">
  <div class="tile-head"><svg width="52" height="44" viewBox="0 0 52 44"><rect x="8" y="8" width="36" height="24" rx="2" fill="none" stroke="#fff" stroke-width="3.5"/><path d="M2 35h48l-4 5H6z" fill="#fff"/></svg><div class="tile-title">Designa<br>your shop</div></div>
  <p class="tile-text">Choose from finished appearance templates or create your own graphic profile with a few clicks.</p>
  <div class="read-more">Read more <svg width="11" height="11" viewBox="0 0 11 11"><circle cx="5.5" cy="5.5" r="5.5" fill="#fff"/><path d="M4.5 3l2.5 2.5L4.5 8" stroke="#1591d4" stroke-width="1.6" fill="none"/></svg></div>
</div>
<div class="abs tile dark" style="left:776px;top:1030px">
  <div class="tile-head"><svg width="50" height="44" viewBox="0 0 50 44"><path d="M3 36a22 22 0 1 1 44 0z" fill="#fff"/><circle cx="12" cy="28" r="3" fill="#3b3b3b"/><circle cx="15" cy="17" r="3" fill="#3b3b3b"/><circle cx="25" cy="12" r="3" fill="#3b3b3b"/><circle cx="38" cy="28" r="3" fill="#3b3b3b"/><path d="M25 32l9-15" stroke="#3b3b3b" stroke-width="3.5"/><circle cx="25" cy="32" r="4" fill="#3b3b3b"/></svg><div class="tile-title">Smart<br>dashboard</div></div>
  <p class="tile-text">On the home page of your online store, you get an overview about the last incoming orders, analysis and statistics on sales, etc.</p>
  <div class="read-more">Read more <svg width="11" height="11" viewBox="0 0 11 11"><circle cx="5.5" cy="5.5" r="5.5" fill="#fff"/><path d="M4.5 3l2.5 2.5L4.5 8" stroke="#3b3b3b" stroke-width="1.6" fill="none"/></svg></div>
</div>

<section class="features">
  <h2 class="abs section-title feature-title">KEY FEATURE</h2>
  <p class="abs feature-sub">Sed ut perspiciatis unde omnis iste natus error sit voluptatem accusantium doloremque laudantium, totam rem aperiam.</p>

  <div class="abs feature" style="left:99px;top:168px">
    <div class="feature-icon"><svg width="38" height="30" viewBox="0 0 38 30"><path d="M2 2v26h34" fill="none" stroke="#222" stroke-width="2.5"/><path d="M7 22l9-9 6 5 11-11" fill="none" stroke="#222" stroke-width="3.5"/><path d="M27 6h7v7" fill="none" stroke="#222" stroke-width="3"/></svg></div>
    <div class="feature-name">Quis autem vel eum iure</div>
    <p class="feature-text">Sed ut perspiciatis unde omnis iste natus error sit voluptatem accusntium doloremque laudantium</p>
    <div class="feature-more">Read More <span style="font-size:10px">↘</span></div>
  </div>
  <div class="abs feature" style="left:456px;top:168px">
    <div class="feature-icon"><svg width="32" height="38" viewBox="0 0 32 38"><ellipse cx="16" cy="6" rx="15" ry="5" fill="#222"/><path d="M1 10c0 6 30 6 30 0v7c0 6-30 6-30 0z" fill="#222"/><path d="M1 21c0 6 30 6 30 0v10c0 7-30 7-30 0z" fill="#222"/></svg></div>
    <div class="feature-name">Quis autem vel eum iure</div>
    <p class="feature-text">Sed ut perspiciatis unde omnis iste natus error sit voluptatem accusntium doloremque laudantium</p>
    <div class="feature-more">Read More <span style="font-size:10px">↘</span></div>
  </div>
  <div class="abs feature" style="left:803px;top:168px">
    <div class="feature-icon"><svg width="38" height="32" viewBox="0 0 38 32"><rect x="13" y="2" width="12" height="6" fill="none" stroke="#222" stroke-width="3"/><rect x="2" y="8" width="34" height="22" rx="3" fill="#222"/><path d="M19 12v14M12 19h14" stroke="#fff" stroke-width="4"/></svg></div>
    <div class="feature-name">Quis autem vel eum iure</div>
    <p class="feature-text">Sed ut perspiciatis unde omnis iste natus error sit voluptatem accusntium doloremque laudantium</p>
    <div class="feature-more">Read More <span style="font-size:10px">↘</span></div>
  </div>

  <div class="abs feature" style="left:99px;top:333px">
    <div class="feature-icon"><svg width="38" height="34" viewBox="0 0 38 34"><rect x="2" y="2" width="34" height="23" rx="2" fill="#222"/><rect x="5" y="5" width="28" height="17" fill="#fff"/><rect x="15" y="25" width="8" height="5" fill="#222"/><rect x="10" y="29" width="18" height="3" fill="#222"/></svg></div>
    <div class="feature-name">Quis autem vel eum iure</div>
    <p class="feature-text">Sed ut perspiciatis unde omnis iste natus error sit voluptatem accusntium doloremque laudantium</p>
    <div class="feature-more">Read More <span style="font-size:10px">↘</span></div>
  </div>
  <div class="abs feature" style="left:456px;top:333px">
    <div class="feature-icon"><svg width="42" height="34" viewBox="0 0 42 34"><ellipse cx="16" cy="13" rx="15" ry="11" fill="#222"/><path d="M6 21l-4 8 10-5z" fill="#222"/><ellipse cx="28" cy="20" rx="12" ry="9" fill="#222" stroke="#fff" stroke-width="2"/><path d="M36 26l4 6-9-4z" fill="#222"/></svg></div>
    <div class="feature-name">Quis autem vel eum iure</div>
    <p class="feature-text">Sed ut perspiciatis unde omnis iste natus error sit voluptatem accusntium doloremque laudantium</p>
    <div class="feature-more">Read More <span style="font-size:10px">↘</span></div>
  </div>
  <div class="abs feature" style="left:803px;top:333px">
    <div class="feature-icon"><svg width="38" height="28" viewBox="0 0 38 28"><rect x="2" y="2" width="34" height="24" rx="2" fill="none" stroke="#222" stroke-width="3"/><path d="M3 4l16 13L35 4" fill="none" stroke="#222" stroke-width="3"/></svg></div>
    <div class="feature-name">Quis autem vel eum iure</div>
    <p class="feature-text">Sed ut perspiciatis unde omnis iste natus error sit voluptatem accusntium doloremque laudantium</p>
    <div class="feature-more">Read More <span style="font-size:10px">↘</span></div>
  </div>
</section>

<h2 class="abs news-title">LATEST NEWS</h2>
<svg class="abs news-arrows" width="34" height="14" viewBox="0 0 34 14"><path d="M2 7h10M2 7l4-4M2 7l4 4" stroke="#222" stroke-width="1.8" fill="none"/><path d="M22 7h10M32 7l-4-4M32 7l-4 4" stroke="#222" stroke-width="1.8" fill="none"/></svg>

<div class="abs news-photo" style="left:97px;background:linear-gradient(135deg,#e7a660,#c8794b 55%,#5aa6a4)" role="img" aria-label="Hands around a table with a tablet and colourful paper speech bubbles"></div>
<article class="abs news-body" style="left:310px">
  <h3>Nulla at diam ornare, aliquam urna</h3>
  <div class="news-date">MAY 25, 2016</div>
  <p>Nulla at diam ornare, aliquam urna vel, commodo urna. Nam id risus a est luctus consectetur quis eget libero. Suspendisse potenti. Pellentesque habitant morbi tristique senectus</p>
  <div class="news-more">Read More +</div>
</article>
<div class="abs news-photo" style="left:630px;background:linear-gradient(135deg,#cfd3d6,#9aa2a8 55%,#6d645c)" role="img" aria-label="Person using a smartphone in front of a laptop on a desk"></div>
<article class="abs news-body" style="left:841px">
  <h3>Nulla at diam ornare, aliquam urna</h3>
  <div class="news-date">MAY 25, 2016</div>
  <p>Nulla at diam ornare, aliquam urna vel, commodo urna. Nam id risus a est luctus consectetur quis eget libero. Suspendisse potenti. Pellentesque habitant morbi tristique senectus</p>
  <div class="news-more">Read More +</div>
</article>

<footer class="footer">
  <div class="abs brand">KELPORIA</div>
  <div class="abs contact">
    <div class="contact-row"><svg width="16" height="20" viewBox="0 0 16 20"><path d="M8 1a6.5 6.5 0 0 0-6.5 6.5C1.5 12 8 19 8 19s6.5-7 6.5-11.5A6.5 6.5 0 0 0 8 1z" fill="none" stroke="#fff" stroke-width="1.5"/><circle cx="8" cy="7.5" r="2.3" fill="none" stroke="#fff" stroke-width="1.5"/></svg><div>Kelporia<br>412 Linden Quay, Suite 18</div></div>
    <div class="contact-row"><svg width="18" height="18" viewBox="0 0 18 18"><path d="M4 1l3 4-2 2c1 2 4 5 6 6l2-2 4 3-2 3C8 17 1 10 1 4z" fill="none" stroke="#fff" stroke-width="1.4"/></svg><div>Phone : 1-800-555-0147</div></div>
    <div class="contact-row"><svg width="18" height="14" viewBox="0 0 18 14"><rect x="1" y="1" width="16" height="12" fill="none" stroke="#fff" stroke-width="1.4"/><path d="M1 1l8 7 8-7" fill="none" stroke="#fff" stroke-width="1.4"/></svg><div>info@kelporia.example</div></div>
  </div>
  <div class="abs signup">
    <h4>Sign up to receive email</h4>
    <p>Excepteur sint occaecat cupidatat non proident, sunt in culpa qui Nemo enim ipsam voluptatem</p>
    <div class="signup-input">Enter Name</div>
    <div class="btn-subscribe">Subscribe</div>
  </div>
  <nav class="abs links">
    <h4>Quick links</h4>
    <ul><li>Home</li><li>About Us</li><li>Our Services</li><li>Blog</li><li>Contact Us</li></ul>
  </nav>
  <div class="abs social">
    <h4>Social media</h4>
    <ul>
      <li><span class="dot"></span>Friendline</li>
      <li><span class="dot"></span>Chirpwire</li>
      <li><span class="dot"></span>Circleplus</li>
      <li><span class="dot"></span>Viewtube</li>
    </ul>
  </div>
</footer>
<div class="copyright">Copyright © Kelporia 2016. All rights reserved.</div>

</body>
</html>
```